Help our Crumb Parlour find our winning design! We're looking for a business card....

We’re a Crumb Parlour in NY specializing in custom-made cakes and unique desserts.
Our cakes combine flavor and art, each designed to match customer’s special event and theme.
We’d like a unique business card with a clean design that will combine French chic and artistic look & feel.
We’d like to differentiate ourselves from standard bakeries, please don’t offer cupcake images :-)
Our logo is peach-pink and brown and we’d love to use these colors ( . Another color that can be added is gold - or feel free to suggest!

Target Market(s)

Women, ages 25-55

Industry/Entity Type

Boutique

Contact Information for Business Card

Text on card:
Logo
Crumb Parlour by Dana Whitfield

www.xxxxxxxx.com
xxx@xxxxx.com
(516) xxx-xxxx
F – xxxxxxxxxx
IG - xxxxxxxxx

Font styles to use
Sans Serif
Script

Requirements
Must have
• Logo
• Clean look
• French chic and artistic look & feel.
Nice to have
• Damask pattern
Should not have
• Cupcake images

```html
<!DOCTYPE html>
<html lang="en">
<head>
<meta charset="utf-8">
<title>Crumb Parlour – Business Card</title>
<link href="https://fonts.googleapis.com/css2?family=Cormorant+Garamond:wght@500&display=swap" rel="stylesheet">
<style>
  :root {
    --backdrop: #e4e4e4;
    --blush: #dfa4ab;
    --blush-deep: #d3929a;
    --magenta: #e0197d;
    --magenta-edge: #f06aa9;
    --peach: #eda08f;
    --peach-soft: #f6ddd7;
    --cocoa: #3a2c2a;
    --cocoa-deep: #2c211f;
    --gold: #c9a13c;
    --gold-light: #f1d77d;
    --ink: #2f2523;
    --white: #ffffff;
  }
  * { margin: 0; padding: 0; box-sizing: border-box; }
  html, body { width: 1200px; height: 852px; overflow: hidden; background: var(--backdrop); }
  .canvas { position: relative; width: 1200px; height: 852px; }

  .card {
    position: absolute; width: 540px; height: 309px; top: 271px;
    border-radius: 22px; overflow: hidden;
    box-shadow: 0 6px 18px rgba(0,0,0,.18);
  }
  .card--front { left: 40px; background: var(--blush); }
  .card--back { left: 620px; background: var(--white); }

  /* front */
  .damask-field {
    position: absolute; inset: 0;
    background: linear-gradient(135deg, var(--blush) 0%, var(--blush-deep) 50%, var(--blush) 100%);
  }
  .ribbon {
    position: absolute; left: 0; right: 0; top: 142px; height: 36px;
    background: var(--magenta);
    border-top: 2px solid var(--magenta-edge); border-bottom: 2px solid var(--magenta-edge);
  }
  .plaque {
    position: absolute; left: 110px; top: 82px; width: 320px; height: 150px;
    background: var(--white); border: 2px solid var(--peach); border-radius: 40px;
    box-shadow: 0 2px 6px rgba(0,0,0,.15);
    display: flex; align-items: center; justify-content: center;
  }

  .brand-name {
    font-family: "Cormorant Garamond", serif; font-weight: 500; font-style: normal;
    color: var(--ink); font-size: 40px; line-height: 1; white-space: nowrap;
    display: flex; align-items: center; gap: 12px;
  }
  .brand-dot { width: 10px; height: 10px; border-radius: 50%; background: var(--peach); flex: none; }

  /* back */
  .flourish {
    position: absolute;
    background: radial-gradient(ellipse at center, var(--peach-soft) 0%, rgba(255,255,255,0) 70%);
  }
  .flourish--top { right: 10px; top: 0; width: 220px; height: 110px; }
  .flourish--left { left: 0; top: 60px; width: 130px; height: 130px; }
  .logo-block {
    position: absolute; left: 60px; top: 40px; width: 340px; height: 120px;
    display: flex; align-items: center; justify-content: center;
  }
  .gold-rule {
    position: absolute; left: 0; right: 0; top: 178px; height: 4px;
    background: linear-gradient(90deg, var(--gold), var(--gold-light), var(--gold));
  }
  .cocoa-panel {
    position: absolute; left: 0; right: 0; top: 182px; bottom: 0;
    background: linear-gradient(180deg, var(--cocoa) 0%, var(--cocoa-deep) 100%);
  }
  .flourish--dark {
    position: absolute; right: 0; top: 0; width: 240px; height: 127px;
    background: radial-gradient(ellipse at 70% 30%, rgba(255,255,255,.07) 0%, rgba(255,255,255,0) 70%);
  }
  .contact-list, .social-list {
    position: absolute; list-style: none;
    font-family: "Cormorant Garamond", serif; font-weight: 500;
    color: var(--peach); font-size: 17px; line-height: 22px; white-space: nowrap;
  }
  .contact-list { left: 22px; bottom: 16px; }
  .social-list { right: 22px; top: 14px; }
  .contact-list li, .social-list li { display: flex; align-items: center; gap: 10px; }
  .icon { width: 12px; height: 12px; flex: none; }
  .social-mark { width: 12px; height: 12px; background: var(--peach); border-radius: 2px; flex: none; }
</style>
</head>
<body>
<main class="canvas">

  <section class="card card--front" aria-label="Card front">
    <div class="damask-field" role="img" aria-label="Tone-on-tone pink damask pattern"></div>
    <div class="ribbon"></div>
    <div class="plaque">
      <div class="brand-name"><span class="brand-dot"></span>Crumb Parlour</div>
    </div>
  </section>

  <section class="card card--back" aria-label="Card back">
    <div class="flourish flourish--top" role="img" aria-label="Faint pink floral flourish"></div>
    <div class="flourish flourish--left" role="img" aria-label="Faint pink floral flourish"></div>
    <div class="logo-block">
      <div class="brand-name"><span class="brand-dot"></span>Crumb Parlour</div>
    </div>
    <div class="gold-rule"></div>
    <div class="cocoa-panel">
      <div class="flourish--dark" role="img" aria-label="Subtle brown floral flourish"></div>
      <ul class="social-list">
        <li><span class="social-mark"></span>CrumbParlourNYCakes</li>
        <li><span class="social-mark"></span>CrumbParlourNYCakes</li>
      </ul>
      <ul class="contact-list">
        <li>
          <svg class="icon" viewBox="0 0 12 12" aria-hidden="true"><path d="M2 1h3l1 3-2 1a7 7 0 0 0 3 3l1-2 3 1v3c-6 1-10-3-9-9z" fill="#eda08f"/></svg>
          (516) 555-0182
        </li>
        <li>
          <svg class="icon" viewBox="0 0 12 12" aria-hidden="true"><circle cx="6" cy="6" r="5" fill="none" stroke="#eda08f" stroke-width="1.2"/><path d="M1 6h10M6 1c-3 3-3 7 0 10M6 1c3 3 3 7 0 10" fill="none" stroke="#eda08f" stroke-width="1"/></svg>
          www.CrumbParlourNY.com
        </li>
        <li>
          <svg class="icon" viewBox="0 0 12 12" aria-hidden="true"><rect x="0.5" y="2" width="11" height="8" fill="none" stroke="#eda08f" stroke-width="1.2"/><path d="M1 2.5l5 4 5-4" fill="none" stroke="#eda08f" stroke-width="1.2"/></svg>
          dana@CrumbParlourNY.com
        </li>
      </ul>
    </div>
  </section>

</main>
</body>
</html>
```